Product Offering / Information Flyer Template

We are looking for a trifold / door hanger style (Folded Letter Dual Sided) marketing piece to announce and explain a new product offering for Fiber To The Home.

We are looking to make the front display very clear of the message and project status, inside would have an image or two and details about the project and information about the product release and how to register for product services.

I'd also like this to be KRDL ready so the back fold should have areas for address label, return address, and postage. Please take in to consideration on the rear flap design. Thank you.

Target Market(s)

Residential Customers

Industry/Entity Type

Internet Service Provider

Font styles to use
Sans Serif

Colors
add136
0355a3
ec1f27

Requirements
Must have
• This is a new fiber to the home deployment in the area. People in this area have been waiting for someone to bring this service to the area for 8 years now and we are finally the ones to do it. This flier needs to be eye catching, exciting, serious.
• 1) Exciting Announcement of a new service / product in the community.
• 2) Coupon code area with coupon value and area for rules (fine print)
• 3) Service Offering Description
• 4) Explanation of why this service is important
• 5) Time Frame for availability of service
• 6) Steps to sign up
• ***Look and feel of attached company logo
Nice to have
• Flash, eye catching
Should not have
• Specifics. I am looking for a template, placeholders for text and information. You can makeup whatever for the moment, we can change the copy out later.

```html
<!DOCTYPE html>
<html lang="en">
<head>
<meta charset="utf-8">
<title>Brightline Fiber – Trifold Mailer</title>
<link rel="stylesheet" href="https://fonts.googleapis.com/css2?family=Lato:ital,wght@0,400;0,700;0,900;1,700&family=Merriweather:wght@700&family=Oswald:wght@500;600&display=swap">
<style>
  :root{
    --green:#add136;
    --blue:#0355a3;
    --blue-dark:#023f7c;
    --navy:#0b2a52;
    --red:#ec1f27;
    --white:#ffffff;
    --ink:#222222;
    --stage:#3b3b3b;
    --row:#dfe9f5;
  }
  *{box-sizing:border-box;margin:0;padding:0}
  html,body{width:902px;height:1200px;overflow:hidden;background:var(--stage)}
  body{font-family:"Lato",sans-serif;color:var(--ink)}
  .canvas{position:relative;width:902px;height:1200px;overflow:hidden;background:var(--stage)}

  .spread{position:absolute;left:21px;top:24px;width:860px;height:611px;display:flex;box-shadow:0 6px 18px rgba(0,0,0,.5)}
  .panel{position:relative;height:611px;overflow:hidden;flex:none}
  .panel svg.layer{position:absolute;inset:0;width:100%;height:100%}

  /* inside panel */
  .panel--inside{width:292px;background:linear-gradient(180deg,var(--blue) 0%,var(--blue-dark) 100%);color:var(--white)}
  .section-pill{position:absolute;left:0;background:var(--white);color:var(--navy);font-family:"Merriweather",serif;font-weight:700;font-size:10px;padding:3px 12px 3px 20px;border-radius:0 10px 10px 0}
  .section-pill--about{top:30px}
  .section-pill--service{top:164px}
  .body-copy{position:absolute;left:20px;width:256px;font-size:8.6px;line-height:1.27;text-align:justify}
  .body-copy--about{top:52px}
  .body-copy--service{top:186px}
  .bullets{position:absolute;left:20px;top:250px;list-style:none;font-size:8.6px;font-weight:700;font-style:italic;line-height:1.85}
  .bullets li::before{content:"";display:inline-block;width:5px;height:5px;border-radius:50%;background:var(--white);margin-right:10px;vertical-align:1px}
  .price-list{position:absolute;left:17px;top:334px;width:256px;height:116px;background:var(--white);border-radius:12px;overflow:hidden}
  .price-list__title{background:var(--green);color:var(--navy);text-align:center;font-size:11px;font-weight:700;padding:4px 0}
  .price-list__row{display:flex;justify-content:space-between;margin:6px 8px 0;padding:6px 6px;background:var(--row);border-radius:4px;color:var(--navy);font-size:8.4px;font-weight:700}
  .coupon-badge{position:absolute;left:23px;top:480px;width:88px;height:88px;border-radius:50%;background:var(--blue);border:3px solid var(--white);box-shadow:0 0 0 2px var(--blue);color:var(--white);text-align:center}
  .coupon-badge__value{display:block;font-family:"Oswald",sans-serif;font-weight:600;font-size:24px;line-height:1;margin-top:16px}
  .coupon-badge__value small{font-size:11px;display:inline-block;transform:rotate(-90deg);vertical-align:4px}
  .coupon-badge__note{display:block;font-size:7.6px;font-weight:700;line-height:1.2;margin-top:4px;padding:0 12px}
  .coupon-title{position:absolute;left:132px;top:500px;font-family:"Oswald",sans-serif;font-weight:600;font-size:16px;color:var(--white)}
  .coupon-code{position:absolute;left:128px;top:526px;width:120px;padding:2px 0;text-align:center;background:var(--white);border:2px solid var(--red);border-radius:5px;color:var(--blue);font-weight:700;font-size:11.5px;letter-spacing:.5px}
  .contact-bar{position:absolute;left:18px;bottom:9px;display:flex;gap:12px;font-size:6.8px;color:var(--white);align-items:center}
  .contact-bar span{display:flex;align-items:center;gap:3px}
  .contact-bar svg{width:7px;height:7px}

  /* mailer panel */
  .panel--mailer{width:282px;background:var(--white)}
  .stamp-box{position:absolute;left:20px;top:91px;width:68px;height:64px;border:1px solid #555}
  .address-line{position:absolute;top:91px;height:240px;width:1px;background:#777}
  .return-address{position:absolute;left:26px;top:470px;width:160px;transform:rotate(-90deg);transform-origin:top left}
  .return-address strong{display:block;font-size:8.6px;font-weight:700;color:var(--ink)}
  .return-address p{font-size:6.6px;line-height:1.3;margin-top:3px;color:#444;width:120px}

  /* cover panel */
  .panel--cover{width:286px;background:var(--white)}
  .brand{position:absolute;left:0;right:0;top:38px;text-align:center}
  .brand__name{display:inline-flex;align-items:center;gap:6px;font-family:"Lato",sans-serif;font-weight:900;font-size:19px;color:var(--blue)}
  .brand__mark{width:12px;height:12px;background:var(--green)}
  .brand__tagline{display:block;font-size:8.4px;font-weight:700;color:var(--red);margin-top:1px}
  .cover-photo{position:absolute;left:0;top:104px;width:286px;height:366px;background:radial-gradient(circle at 62% 38%,#e9f0f8 0%,#a9bfdc 38%,#5f7fb0 70%,#c9d7ea 100%)}
  .cover-headline{position:absolute;right:14px;top:470px;font-family:"Oswald",sans-serif;font-weight:600;font-size:18.5px;line-height:1.2;text-align:left}
  .cover-headline .dark{color:var(--navy)}
  .cover-headline .blue{color:var(--blue)}
  .cover-headline .red{color:var(--red)}
  .cover-url{position:absolute;left:0;right:0;bottom:14px;text-align:center;font-size:9px;font-weight:700;letter-spacing:1.2px;color:var(--navy)}

  /* flat front / back */
  .view{position:absolute;top:660px;width:220px;height:470px}
  .view--front{left:210px}
  .view--back{left:480px}
  .view .panel{transform:scale(.77);transform-origin:top left;box-shadow:0 6px 18px rgba(0,0,0,.5)}
  .view--back .panel{width:286px}
  .view-label{position:absolute;top:1147px;width:220px;text-align:center;font-size:24px;font-weight:700;color:var(--white)}
</style>
</head>
<body>
<main class="canvas">

  <section class="spread">
    <!-- Inside details panel -->
    <article class="panel panel--inside">
      <svg class="layer" viewBox="0 0 292 611" preserveAspectRatio="none" aria-hidden="true">
        <path d="M0 470 Q150 448 292 462 V611 H0Z" fill="var(--white)" opacity=".9"/>
        <path d="M0 476 Q150 455 292 468 V611 H0Z" fill="var(--green)"/>
        <path d="M0 580 Q150 566 292 578 V611 H0Z" fill="var(--blue)"/>
      </svg>
      <h2 class="section-pill section-pill--about">About us</h2>
      <p class="body-copy body-copy--about">Lorem Ipsum is simply dummy text of the printing and typesetting industry. Lorem Ipsum has been the industry's standard dummy text ever since the 1500s, when an unknown printer took a galley of type and scrambled it to make a type specimen book. It has survived not only five centuries, but also the leap into electronic typesetting, remaining essentially unchanged. It was popularised in the 1960s with the release of Letraset sheets containing Lorem Ipsum passages, and more recently with desktop publishing software.</p>
      <h2 class="section-pill section-pill--service">Service Offering Description</h2>
      <p class="body-copy body-copy--service">Lorem Ipsum is simply dummy text of the printing and typesetting industry. Lorem Ipsum has been the industry's standard dummy text ever since the 1500s, when an unknown printer took a galley of type and scrambled it to make a type specimen book. em Ipsum.</p>
      <ul class="bullets">
        <li>Lorem Ipsum is simply dummy text of the printing</li>
        <li>And typesetting industry.</li>
        <li>Lorem Ipsum has been the industry's standard dummy</li>
        <li>Text ever since the 1500s, when an unknown printer</li>
      </ul>
      <div class="price-list">
        <h3 class="price-list__title">Price List</h3>
        <div class="price-list__row"><span>Lorem Ipsum is simply dummy text.....................</span><span>£000</span></div>
        <div class="price-list__row"><span>Lorem Ipsum is simply dummy text.....................</span><span>£000</span></div>
        <div class="price-list__row"><span>Lorem Ipsum is simply dummy text.....................</span><span>£000</span></div>
      </div>
      <div class="coupon-badge">
        <span class="coupon-badge__value">10%<small>OFF</small></span>
        <span class="coupon-badge__note">Lorem Ipsum is simply dummy</span>
      </div>
      <p class="coupon-title">COUPONE CODE!</p>
      <p class="coupon-code">XXXXX1234567</p>
      <footer class="contact-bar">
        <span><svg viewBox="0 0 10 10"><path d="M2 1 L4 1 L5 3.5 L3.8 4.5 Q4.8 6.2 5.5 6.3 L6.5 5 L9 6 L9 8 Q9 9 8 9 Q1 8.5 1 2 Q1 1 2 1Z" fill="currentColor"/></svg>xxxxxxxxxx</span>
        <span><svg viewBox="0 0 10 10"><rect x="1" y="2" width="8" height="6" fill="none" stroke="currentColor"/><path d="M1 2 L5 5.5 L9 2" fill="none" stroke="currentColor"/></svg>info@companyname.com</span>
        <span><svg viewBox="0 0 10 10"><path d="M5 9.5 Q1.5 5.5 1.5 3.7 A3.5 3.5 0 0 1 8.5 3.7 Q8.5 5.5 5 9.5Z" fill="currentColor"/><circle cx="5" cy="3.7" r="1.2" fill="var(--blue)"/></svg>Company Address here</span>
      </footer>
    </article>

    <!-- Mailer panel -->
    <article class="panel panel--mailer">
      <svg class="layer" viewBox="0 0 282 611" preserveAspectRatio="none" aria-hidden="true">
        <path d="M0 0 H282 V30 Q140 34 0 64Z" fill="var(--green)"/>
        <path d="M0 64 Q140 34 282 30 V38 Q140 44 0 74Z" fill="var(--blue)"/>
        <path d="M0 74 Q140 44 282 38 V42 Q140 49 0 78Z" fill="var(--red)"/>
        <path d="M0 470 Q120 520 282 548 V611 H0Z" fill="var(--green)"/>
        <path d="M0 500 Q140 545 282 562 V572 Q140 556 0 512Z" fill="var(--blue)"/>
        <path d="M0 512 Q140 556 282 572 V578 Q140 562 0 518Z" fill="var(--red)"/>
        <path d="M0 486 Q140 530 282 552 V562 Q140 545 0 500Z" fill="var(--white)"/>
      </svg>
      <div class="stamp-box"></div>
      <span class="address-line" style="left:163px"></span>
      <span class="address-line" style="left:200px"></span>
      <span class="address-line" style="left:239px"></span>
      <div class="return-address">
        <strong>Lorem Ipsum is simply dummy text</strong>
        <p>Lorem Ipsum is simply dummy text of the printing and typesetting industry. Lorem Ipsum has been the industry's standard dummy text</p>
      </div>
    </article>

    <!-- Cover panel -->
    <article class="panel panel--cover">
      <div class="cover-photo" role="img" aria-label="Glass globe with a red-roofed house and a woman with a laptop celebrating, over a blue digital data backdrop"></div>
      <svg class="layer" viewBox="0 0 286 611" preserveAspectRatio="none" aria-hidden="true">
        <path d="M0 0 H286 V84 Q140 118 0 86Z" fill="var(--white)"/>
        <path d="M0 86 Q140 118 286 84 V94 Q140 128 0 96Z" fill="var(--blue)"/>
        <path d="M0 96 Q140 128 286 94 V99 Q140 134 0 101Z" fill="var(--red)"/>
        <path d="M0 101 Q140 134 286 99 V105 Q140 140 0 107Z" fill="var(--green)"/>
        <path d="M0 448 Q140 470 286 430 V611 H0Z" fill="var(--green)"/>
        <path d="M0 548 Q150 540 286 488 V504 Q150 556 0 562Z" fill="var(--blue)"/>
        <path d="M0 562 Q150 556 286 504 V510 Q150 562 0 568Z" fill="var(--red)"/>
        <path d="M0 568 Q150 562 286 510 V611 H0Z" fill="var(--green)"/>
      </svg>
      <div class="brand">
        <span class="brand__name"><span class="brand__mark"></span>Brightline Fiber</span>
        <span class="brand__tagline">Home Internet, Finally Here</span>
      </div>
      <h1 class="cover-headline"><span class="dark">NEW FIBER</span> <span class="blue">TO THE HOME</span><br><span class="red">DEPLOYMENT</span></h1>
      <p class="cover-url">www.yourwebsitename.com</p>
    </article>
  </section>

  <!-- Front view -->
  <div class="view view--front">
    <article class="panel panel--cover">
      <div class="cover-photo" role="img" aria-label="Glass globe with a red-roofed house and a woman with a laptop celebrating, over a blue digital data backdrop"></div>
      <svg class="layer" viewBox="0 0 286 611" preserveAspectRatio="none" aria-hidden="true">
        <path d="M0 0 H286 V84 Q140 118 0 86Z" fill="var(--white)"/>
        <path d="M0 86 Q140 118 286 84 V94 Q140 128 0 96Z" fill="var(--blue)"/>
        <path d="M0 96 Q140 128 286 94 V99 Q140 134 0 101Z" fill="var(--red)"/>
        <path d="M0 101 Q140 134 286 99 V105 Q140 140 0 107Z" fill="var(--green)"/>
        <path d="M0 448 Q140 470 286 430 V611 H0Z" fill="var(--green)"/>
        <path d="M0 548 Q150 540 286 488 V504 Q150 556 0 562Z" fill="var(--blue)"/>
        <path d="M0 562 Q150 556 286 504 V510 Q150 562 0 568Z" fill="var(--red)"/>
        <path d="M0 568 Q150 562 286 510 V611 H0Z" fill="var(--green)"/>
      </svg>
      <div class="brand">
        <span class="brand__name"><span class="brand__mark"></span>Brightline Fiber</span>
        <span class="brand__tagline">Home Internet, Finally Here</span>
      </div>
      <p class="cover-headline"><span class="dark">NEW FIBER</span> <span class="blue">TO THE HOME</span><br><span class="red">DEPLOYMENT</span></p>
      <p class="cover-url">www.yourwebsitename.com</p>
    </article>
  </div>
  <p class="view-label" style="left:210px">Front</p>

  <!-- Back view -->
  <div class="view view--back">
    <article class="panel panel--mailer">
      <svg class="layer" viewBox="0 0 282 611" preserveAspectRatio="none" aria-hidden="true">
        <path d="M0 0 H282 V30 Q140 34 0 64Z" fill="var(--green)"/>
        <path d="M0 64 Q140 34 282 30 V38 Q140 44 0 74Z" fill="var(--blue)"/>
        <path d="M0 74 Q140 44 282 38 V42 Q140 49 0 78Z" fill="var(--red)"/>
        <path d="M0 470 Q120 520 282 548 V611 H0Z" fill="var(--green)"/>
        <path d="M0 500 Q140 545 282 562 V572 Q140 556 0 512Z" fill="var(--blue)"/>
        <path d="M0 512 Q140 556 282 572 V578 Q140 562 0 518Z" fill="var(--red)"/>
        <path d="M0 486 Q140 530 282 552 V562 Q140 545 0 500Z" fill="var(--white)"/>
      </svg>
      <div class="stamp-box"></div>
      <span class="address-line" style="left:163px"></span>
      <span class="address-line" style="left:200px"></span>
      <span class="address-line" style="left:239px"></span>
      <div class="return-address">
        <strong>Lorem Ipsum is simply dummy text</strong>
        <p>Lorem Ipsum is simply dummy text of the printing and typesetting industry. Lorem Ipsum has been the industry's standard dummy text</p>
      </div>
    </article>
  </div>
  <p class="view-label" style="left:480px">Back</p>

</main>
</body>
</html>
```